Transfer Pricing Flyer

This is a technical document meant for CEOs and CFOs. Intent is to make a complex technical subject simple. I have also added our logo with this document for you to use it appropriately. you can also peruse our website for further details or write to me.

hi all have uploaded our logo to our brief. pl use the logo while designing

Reason: Not sufficient good designs have been recievved

Industry/Entity Type

Pricing

Colors
34a6d7
85cae6
cde9f5
ceddec
85abd2
0555a3
0255a3

```html
<!DOCTYPE html>
<html lang="en">
<head>
<meta charset="utf-8">
<title>Transfer Pricing Demystified – Karvan Advisors LLP</title>
<link rel="stylesheet" href="https://fonts.googleapis.com/css2?family=Open+Sans:ital,wght@0,400;0,600;0,700;1,600;1,700&family=Raleway:wght@100;200;300&display=swap">
<style>
  :root {
    --navy: #0b55a6;
    --navy-deep: #0a4a94;
    --navy-band: #0c4f9c;
    --band-light: #2e6db0;
    --band-mid: #1a5ea6;
    --sky: #85cae6;
    --cyan: #5cc2ee;
    --pale: #cde9f5;
    --ink: #14253d;
    --white: #ffffff;
  }
  * { margin: 0; padding: 0; box-sizing: border-box; }
  html, body { width: 1200px; height: 812px; overflow: hidden; background: #fff; }
  body { font-family: "Open Sans", Arial, sans-serif; }
  .flyer { position: relative; width: 1200px; height: 812px; overflow: hidden; }

  /* Left panel */
  .about-panel { position: absolute; left: 0; top: 0; width: 600px; height: 812px; background: var(--navy); color: var(--white); }
  .portrait-photo { position: absolute; left: 342px; top: 0; width: 220px; height: 300px;
    background: linear-gradient(160deg, #dbe8f4 0%, #8fb3d8 40%, #1b4f8e 75%, #0b2f5e 100%); }
  .section-label { position: absolute; left: 35px; font-size: 10px; font-weight: 600; color: var(--cyan); letter-spacing: .2px; }
  .body-copy { position: absolute; left: 35px; font-size: 10px; line-height: 16.8px; text-align: justify; }
  .narrow { width: 288px; letter-spacing: -0.1px; }
  .wide { width: 528px; }
  .practice-list { position: absolute; left: 35px; top: 334px; list-style: none; font-size: 10px; }
  .practice-list li { display: flex; align-items: center; height: 20px; }
  .practice-list svg { width: 9px; height: 9px; margin-right: 7px; flex: none; }

  .brand-block { position: absolute; left: 200px; top: 666px; width: 194px; text-align: center; }
  .brand-mark { width: 94px; height: 44px; margin: 0 auto 7px; background: var(--white);
    display: flex; align-items: center; justify-content: center;
    font-weight: 700; font-size: 14px; color: var(--navy); }
  .brand-name { font-size: 17px; line-height: 20px; }
  .brand-line { font-size: 12px; line-height: 15px; }

  /* Right panel */
  .hero-photo { position: absolute; left: 600px; top: 0; width: 600px; height: 300px;
    background: linear-gradient(135deg, #1c4f8c 0%, #6d95c3 30%, #dfe9f3 55%, #9ab9da 75%, #244f86 100%); }
  .title-band { position: absolute; left: 600px; top: 300px; width: 600px; height: 115px; background: var(--navy-band); }
  .band-strip { position: absolute; top: 0; height: 100%; }
  .title-primary, .title-secondary { position: absolute; left: 634px; font-family: "Raleway", sans-serif;
    white-space: nowrap; transform-origin: left top; }
  .title-primary { top: 301px; font-weight: 100; font-size: 60px; line-height: 60px; color: var(--pale);
    transform: scaleX(0.91); }
  .title-secondary { top: 355px; font-weight: 300; font-size: 54px; line-height: 54px; color: var(--white); }

  .explainer { position: absolute; left: 600px; top: 415px; width: 600px; height: 397px; background: var(--sky); color: var(--ink); }
  .question { position: absolute; left: 35px; top: 20px; font-size: 10.5px; font-weight: 700; color: var(--white); }
  .explainer .body-copy { top: 42px; width: 530px; color: var(--ink); }
  .case-label { position: absolute; font-size: 10px; font-weight: 700; color: var(--ink); }
  .case-note { position: absolute; left: 94px; top: 243px; font-size: 10px; color: var(--ink); }
  .flow-box { position: absolute; background: var(--navy); color: var(--white); text-align: center;
    font-size: 9.5px; line-height: 18px; padding-top: 6px; }
  .flow-box h3 { font-size: 10px; font-style: italic; font-weight: 700; margin-bottom: 2px; }
  .buyer { display: flex; align-items: center; justify-content: center; padding: 0;
    font-size: 10px; font-style: italic; font-weight: 700; }
  .flow-arrows { position: absolute; left: 0; top: 0; }
</style>
</head>
<body>
<main class="flyer">

  <section class="about-panel">
    <div class="portrait-photo" role="img" aria-label="Photo of a smiling senior executive seated at a desk with a lamp and a cup"></div>

    <h2 class="section-label" style="top:34px">ABOUT US</h2>
    <p class="body-copy narrow" style="top:50px">Karvan Advisors LLP, formerly Ramesh Kalyan &amp; Associates, is a contemporary tax, legal and financial solutions provider with a specific focus on Direct, International and Indirect taxation. We deliver research based, value added and customized solutions to our diverse clientele spanning from software to the mining industry. We bring together a harmonious blend of Tax, Legal and Financial expertise and provide a single point contact for our client engagements.</p>
    <p class="body-copy narrow" style="top:192px">We have a diverse team of professionals comprising of chartered accountants, lawyers, cost accountants, bankers and company secretaries with varied industry experience engaging with our clients at various levels. Our values are high quality research based solutions, punctuality and certainty in delivery deadlines and handholding client issues with a personal touch.</p>

    <h2 class="section-label" style="top:317px">OUR CORE PRACTICE AREAS ARE:</h2>
    <ul class="practice-list">
      <li><svg viewBox="0 0 10 10"><circle cx="5" cy="5" r="4.3" fill="none" stroke="#5cc2ee"/><path d="M3.5 3l2 2-2 2" fill="none" stroke="#5cc2ee"/></svg>Structuring Inbound and Outbound investments.</li>
      <li><svg viewBox="0 0 10 10"><circle cx="5" cy="5" r="4.3" fill="none" stroke="#5cc2ee"/><path d="M3.5 3l2 2-2 2" fill="none" stroke="#5cc2ee"/></svg>Tax Structuring and Managing tax structures.</li>
      <li><svg viewBox="0 0 10 10"><circle cx="5" cy="5" r="4.3" fill="none" stroke="#5cc2ee"/><path d="M3.5 3l2 2-2 2" fill="none" stroke="#5cc2ee"/></svg>Domestic and International tax advisory and litigation.</li>
      <li><svg viewBox="0 0 10 10"><circle cx="5" cy="5" r="4.3" fill="none" stroke="#5cc2ee"/><path d="M3.5 3l2 2-2 2" fill="none" stroke="#5cc2ee"/></svg>Transfer Pricing.</li>
      <li><svg viewBox="0 0 10 10"><circle cx="5" cy="5" r="4.3" fill="none" stroke="#5cc2ee"/><path d="M3.5 3l2 2-2 2" fill="none" stroke="#5cc2ee"/></svg>Risk Management for Banks and Financial Institutions.</li>
      <li><svg viewBox="0 0 10 10"><circle cx="5" cy="5" r="4.3" fill="none" stroke="#5cc2ee"/><path d="M3.5 3l2 2-2 2" fill="none" stroke="#5cc2ee"/></svg>Trust and estate taxation.</li>
      <li><svg viewBox="0 0 10 10"><circle cx="5" cy="5" r="4.3" fill="none" stroke="#5cc2ee"/><path d="M3.5 3l2 2-2 2" fill="none" stroke="#5cc2ee"/></svg>Handling complete, end to end international tax and statutory compliance.</li>
      <li><svg viewBox="0 0 10 10"><circle cx="5" cy="5" r="4.3" fill="none" stroke="#5cc2ee"/><path d="M3.5 3l2 2-2 2" fill="none" stroke="#5cc2ee"/></svg>RBI and FEMA compliance and litigation.</li>
    </ul>

    <p class="body-copy wide" style="top:507px">We are affiliated with the Meridian Global Alliance (head quartered in London), one of the top 20 accounting and legal networks in the world having member partners in over 104 countries. We thus have the bandwidth and reach to handle client engagements in more than 100 countries. It is noteworthy to mention that Meridian Global has been voted as the “Association of the Year 2013” by Global Accounting Review.</p>
    <p class="body-copy wide" style="top:574px">Over the past 7 years of our existence, we have successfully engaged with medium to large enterprises from the following industries, IT and ITES, Manufacturing and Auto Ancillary, Banks and Financial Services, Infrastructure and Mining, Heavy Equipments, International Retail, FMCG, Management Consultancy, Entertainment and International Fuel Trade.</p>

    <div class="brand-block">
      <div class="brand-mark">Karvan</div>
      <p class="brand-name">Karvan Advisors LLP</p>
      <p class="brand-line">Tax- Legal- Forensic</p>
      <p class="brand-line">India – Singapore- Dubai- London</p>
      <p class="brand-line">www.karvanadvisors.in</p>
    </div>
  </section>

  <div class="hero-photo" role="img" aria-label="Photo of a business team reviewing charts and reports around a table"></div>

  <div class="title-band">
    <div class="band-strip" style="left:0;width:230px;background:var(--navy-deep)"></div>
    <div class="band-strip" style="left:230px;width:230px;background:var(--band-light)"></div>
    <div class="band-strip" style="left:460px;width:80px;background:var(--band-mid)"></div>
    <div class="band-strip" style="left:540px;width:60px;background:var(--navy-deep)"></div>
  </div>
  <h1 class="title-primary">TRANSFER PRICING</h1>
  <p class="title-secondary">DEMYSTIFIED</p>

  <section class="explainer">
    <h2 class="question">What is the need for Transfer Pricing?</h2>
    <p class="body-copy">Where transactions (both international and domestic) are being conducted between related concerns, there is a possibility that they may not be performed on pure commercial basis. At times, such pricing may also lead to shifting taxes from India to a foreign country or from a high tax entity to a low tax entity within India to save on taxes. Please follow the illustration below:</p>

    <span class="case-label" style="left:36px;top:129px">CASE A</span>
    <div class="flow-box" style="left:95px;top:128px;width:173px;height:91px">
      <h3>Indian Exporter</h3>
      <p>Selling Price = 150</p><p>Cost of Production = 100</p><p>Indian Profits = 50</p>
    </div>
    <div class="flow-box buyer" style="left:429px;top:145px;width:88px;height:56px">German Buyer</div>

    <span class="case-label" style="left:36px;top:243px">CASE B</span>
    <p class="case-note">To avoid taxes – it is always possible to rearrange the business model in the following manner:</p>
    <div class="flow-box" style="left:42px;top:273px;width:173px;height:91px">
      <h3>Indian Exporter</h3>
      <p>Selling Price = 120</p><p>Cost of Production = 100</p><p>Indian Profits = 20</p>
    </div>
    <div class="flow-box" style="left:260px;top:273px;width:145px;height:91px">
      <h3>Dubai Importer &amp; Exporter</h3>
      <p>Selling Price = 150</p><p>Cost of Production = 120</p><p>Indian Profits = 30</p>
    </div>
    <div class="flow-box buyer" style="left:476px;top:290px;width:88px;height:56px">German Buyer</div>

    <svg class="flow-arrows" width="600" height="397" viewBox="0 0 600 397" aria-hidden="true">
      <g stroke="#0b55a6" stroke-width="1.2" fill="#0b55a6">
        <line x1="260" y1="173" x2="398" y2="173"/><path d="M405 173l-8-3.5v7z" stroke="none"/>
        <line x1="222" y1="316" x2="245" y2="316"/><path d="M252 316l-8-3.5v7z" stroke="none"/>
        <line x1="418" y1="316" x2="456" y2="316"/><path d="M463 316l-8-3.5v7z" stroke="none"/>
      </g>
    </svg>
  </section>

</main>
</body>
</html>
```